I need a business card design for a new company that will be doing consulting work around issues of cultural competency, and diversity and inclusion. I would like the design to be crisp and clear with bold but conservative colors and incorporate shades of blue

Target Market(s)

Small businesses, schools, non-profits

Industry/Entity Type

Consulting

Font styles to use
Serif
Sans Serif

Colors
0c5ba6
6b449b
3276b5
0292cd

Requirements
Must have
• A Morrow Venture (name of company)
• Tiru Morrow
• CEO
• tiru@amorrowventure.example
• (215)555-0147

```html
<!DOCTYPE html>
<html lang="en">
<head>
<meta charset="utf-8">
<title>A Morrow Venture – Business Card</title>
<link rel="stylesheet" href="https://fonts.googleapis.com/css2?family=Arimo:wght@400&family=Roboto:wght@400;700&display=swap">
<style>
  :root {
    --backdrop: #1c1c1d;
    --card: #1e1e20;
    --card-edge: #2a2a2c;
    --brand-blue: #3a86d0;
    --text-light: #f2f2f2;
    --silver-dark: #2a2a2c;
    --silver-light: #e6e6e6;
  }
  * { margin: 0; padding: 0; box-sizing: border-box; }
  html, body {
    width: 1200px;
    height: 900px;
    overflow: hidden;
    background: var(--backdrop);
  }
  .canvas {
    width: 1200px;
    height: 900px;
    display: flex;
    flex-direction: column;
    align-items: center;
    justify-content: center;
    gap: 36px;
  }
  .card {
    width: 700px;
    height: 400px;
    background: linear-gradient(135deg, #1a1a1c 0%, var(--card) 55%, #2c2c2e 100%);
    border: 1px solid var(--card-edge);
    box-shadow: 0 14px 30px rgba(0,0,0,0.55);
    position: relative;
  }
  .card-front {
    display: flex;
    align-items: center;
    justify-content: center;
  }
  .front-wordmark {
    font-family: "Arimo", Arial, sans-serif;
    font-size: 30px;
    letter-spacing: 5px;
    text-transform: uppercase;
    background: linear-gradient(90deg, var(--silver-dark) 0%, #6a6a6c 45%, var(--silver-light) 100%);
    -webkit-background-clip: text;
    background-clip: text;
    color: transparent;
  }
  .back-wordmark {
    position: absolute;
    top: 92px;
    left: 0;
    width: 100%;
    text-align: center;
    font-family: "Arimo", Arial, sans-serif;
    font-size: 28px;
    letter-spacing: 4px;
    text-transform: uppercase;
    color: var(--brand-blue);
  }
  .identity {
    position: absolute;
    top: 246px;
    right: 392px;
    text-align: right;
    font-family: "Roboto", Arial, sans-serif;
  }
  .person-name {
    font-size: 27px;
    font-weight: 700;
    letter-spacing: 0.5px;
    text-transform: uppercase;
    color: var(--brand-blue);
    line-height: 1.1;
  }
  .person-title {
    font-size: 17px;
    color: var(--text-light);
    letter-spacing: 1px;
    margin-top: 4px;
  }
  .divider {
    position: absolute;
    top: 250px;
    left: 330px;
    width: 1.5px;
    height: 62px;
    background: var(--text-light);
  }
  .contact {
    position: absolute;
    top: 254px;
    left: 356px;
    list-style: none;
    font-family: "Roboto", Arial, sans-serif;
    font-size: 17px;
    letter-spacing: 1px;
    color: var(--text-light);
  }
  .contact-item {
    display: flex;
    align-items: center;
    gap: 10px;
    height: 27px;
  }
  .contact-icon { width: 13px; height: 13px; flex: none; }
</style>
</head>
<body>
  <main class="canvas">
    <section class="card card-front" aria-label="Card front">
      <p class="front-wordmark">A Morrow Venture</p>
    </section>

    <section class="card card-back" aria-label="Card back">
      <p class="back-wordmark">A Morrow Venture</p>

      <div class="identity">
        <p class="person-name">Tiru Morrow</p>
        <p class="person-title">CEO</p>
      </div>

      <div class="divider"></div>

      <ul class="contact">
        <li class="contact-item">
          <svg class="contact-icon" viewBox="0 0 24 24" aria-hidden="true">
            <path fill="var(--brand-blue)" d="M6.6 10.8a15.1 15.1 0 0 0 6.6 6.6l2.2-2.2a1 1 0 0 1 1-.25 11.4 11.4 0 0 0 3.6.57 1 1 0 0 1 1 1V20a1 1 0 0 1-1 1A17 17 0 0 1 3 4a1 1 0 0 1 1-1h3.5a1 1 0 0 1 1 1c0 1.25.2 2.45.57 3.6a1 1 0 0 1-.25 1z"/>
          </svg>
          <span>(215)555-0147</span>
        </li>
        <li class="contact-item">
          <svg class="contact-icon" viewBox="0 0 24 24" aria-hidden="true">
            <rect x="2" y="5" width="20" height="14" rx="1.5" fill="none" stroke="var(--brand-blue)" stroke-width="2"/>
            <path d="M2.5 6l9.5 7 9.5-7" fill="none" stroke="var(--brand-blue)" stroke-width="2"/>
          </svg>
          <span>tiru@amorrowventure.example</span>
        </li>
      </ul>
    </section>
  </main>
</body>
</html>
```